CEDAR KEEP LOCKERS

Please see the attached. I need a new postcard design with a soccer theme with the headline "Score Big at Cedar Keep Lockers and make it your goal to Store Your Stuff." Everything else that is on the current card stays the same on this new card design, copy, address, phone, etc.

```html
<!DOCTYPE html>
<html lang="en">
<head>
<meta charset="utf-8">
<title>Cedar Keep Lockers – Soccer Postcard</title>
<link href="https://fonts.googleapis.com/css2?family=Bowlby+One&family=Oswald:wght@600;700&family=Open+Sans:wght@700;800&display=swap" rel="stylesheet">
<style>
  :root {
    --page: #e6e6e4;
    --red: #d8184a;
    --green: #0e8a57;
    --dark-green: #0f5a3c;
    --yellow: #fff200;
    --black: #111111;
    --white: #ffffff;
    --sky-top: #1f8fd6;
    --sky-mid: #8fd0f2;
    --sky-low: #e8f6e0;
    --grass-dark: #2f8f1e;
    --grass-light: #7cd43a;
  }
  * { box-sizing: border-box; margin: 0; padding: 0; }
  html, body { width: 816px; height: 1200px; overflow: hidden; }
  body { background: var(--page); position: relative; font-family: "Open Sans", Arial, sans-serif; }

  .card { position: absolute; left: 40px; width: 736px; height: 550px; overflow: hidden; }
  .card--front { top: 30px; background: linear-gradient(180deg, var(--sky-top) 0%, var(--sky-mid) 40%, var(--sky-low) 70%); }
  .card--back { top: 618px; background: linear-gradient(160deg, #8fd3ea 0%, #c9ecd0 40%, #7fd05a 75%, #c4e23c 100%); }

  /* front */
  .headline { position: absolute; left: 28px; top: 14px; font-family: "Bowlby One", "Arial Black", sans-serif; font-size: 82px; line-height: 1; letter-spacing: 1px; color: var(--yellow); text-shadow: 3px 3px 0 var(--black); white-space: nowrap; }
  .headline .hl-red { color: var(--red); }
  .tagline { position: absolute; left: 52px; top: 150px; font-family: "Bowlby One", "Arial Black", sans-serif; line-height: 1.12; }
  .tagline .lead { font-family: "Open Sans", Arial, sans-serif; font-weight: 800; font-size: 38px; color: var(--red); display: block; }
  .tagline .goal { font-family: "Open Sans", Arial, sans-serif; font-weight: 800; font-size: 44px; color: var(--green); display: block; }
  .tagline .store { font-size: 40px; display: block; text-shadow: 2px 2px 0 var(--white); }
  .tagline .red { color: var(--red); }
  .tagline .green { color: var(--green); }

  .brand-front { position: absolute; left: 470px; top: 180px; display: flex; align-items: flex-start; gap: 12px; }
  .brand-square { width: 18px; height: 18px; background: var(--red); margin-top: 14px; flex: none; }
  .brand-name { font-family: "Oswald", Arial, sans-serif; font-weight: 700; font-size: 56px; line-height: 1.05; color: var(--red); text-transform: none; }

  .grass { position: absolute; left: 0; right: 0; bottom: 0; height: 200px; background: linear-gradient(180deg, rgba(124,212,58,0.6) 0%, var(--grass-light) 35%, var(--grass-dark) 100%); }
  .ball-front { position: absolute; left: 172px; top: 346px; width: 210px; height: 210px; border-radius: 50%; background: radial-gradient(circle at 38% 35%, #ffffff 0%, #d5d5d5 55%, #6b6b6b 100%); }

  /* back */
  .ball-back { position: absolute; left: 14px; top: 10px; width: 246px; height: 246px; border-radius: 50%; background: radial-gradient(circle at 45% 40%, #ffffff 0%, #f2f2f2 60%, #cfd8d3 100%); border: 3px solid var(--dark-green); }
  .brand-back { position: absolute; left: 66px; top: 70px; width: 150px; text-align: center; font-family: "Oswald", Arial, sans-serif; font-weight: 700; font-size: 38px; line-height: 1.1; color: var(--red); }

  .contact { position: absolute; left: 38px; top: 280px; width: 214px; height: 200px; background: var(--yellow); border: 4px solid var(--green); text-align: center; }
  .contact .call { font-family: "Oswald", Arial, sans-serif; font-weight: 700; color: var(--red); font-size: 21px; line-height: 1; margin-top: 10px; }
  .contact .call small { display: block; font-size: 14px; margin-top: 2px; }
  .contact .phone { margin: 8px -12px 0; background: var(--red); color: var(--white); font-family: "Oswald", Arial, sans-serif; font-weight: 700; font-size: 26px; line-height: 36px; }
  .contact .address { font-weight: 800; font-size: 12.5px; color: var(--black); margin-top: 10px; line-height: 1.35; }
  .contact .web { position: absolute; left: -12px; right: -12px; bottom: 22px; background: var(--red); color: var(--white); font-weight: 800; font-size: 11.5px; line-height: 22px; }

  .offer { position: absolute; right: 24px; top: 38px; width: 440px; text-align: center; }
  .offer .save { font-family: "Bowlby One", "Arial Black", sans-serif; font-size: 40px; line-height: 1.05; color: var(--black); letter-spacing: 1px; }
  .offer .name { font-family: "Bowlby One", "Arial Black", sans-serif; font-size: 30px; line-height: 1.15; color: var(--red); }
  .offer .today { font-family: "Bowlby One", "Arial Black", sans-serif; font-size: 60px; line-height: 1.05; color: var(--yellow); -webkit-text-stroke: 2px var(--black); text-shadow: 3px 3px 0 var(--black); }

  .features { position: absolute; right: 24px; top: 232px; width: 420px; text-align: right; font-weight: 800; font-size: 15px; line-height: 1.55; color: var(--black); }
  .features p { margin-bottom: 6px; }
  .features .hi { color: var(--red); }
  .features .price-now { color: var(--red); font-size: 18px; }
  .features s { color: var(--red); text-decoration-color: #d8a000; }

  .promo-bar { position: absolute; left: 0; right: 0; bottom: 0; height: 52px; background: rgba(255,242,0,0.55); text-align: center; font-family: "Bowlby One", "Arial Black", sans-serif; font-size: 27px; line-height: 52px; color: var(--red); }
</style>
</head>
<body>

<section class="card card--front">
  <h1 class="headline">SCORE <span class="hl-red">BIG</span> AT</h1>
  <p class="tagline">
    <span class="lead">and make it your</span>
    <span class="goal">GOAL TO</span>
    <span class="store"><span class="red">STORE</span> <span class="green">YOUR STUFF.</span></span>
  </p>
  <div class="grass" role="img" aria-label="Photo of tall green grass against a bright sky"></div>
  <div class="ball-front" role="img" aria-label="Soccer ball resting in the grass"></div>
  <div class="brand-front">
    <span class="brand-square"></span>
    <span class="brand-name">Cedar Keep<br>Lockers</span>
  </div>
</section>

<section class="card card--back" role="img" aria-label="Green and blue paint splash background">
  <div class="ball-back" role="img" aria-label="Soccer ball illustration"></div>
  <div class="brand-back">Cedar Keep Lockers</div>

  <div class="contact">
    <p class="call">CALL TODAY FOR<small>LIMITED TIME SAVINGS!</small></p>
    <p class="phone">(555) 204-7318</p>
    <p class="address">1190 ORCHARD LN<br>FAIRVIEW, IN 46001</p>
    <p class="web">WWW.CEDARKEEPLOCKERS.COM</p>
  </div>

  <div class="offer">
    <p class="save">SAVE BIG WITH</p>
    <p class="name">CEDAR KEEP LOCKERS</p>
    <p class="today">TODAY</p>
  </div>

  <div class="features">
    <p><span class="hi">5X5</span> STANDARD-WAS <s>$54</s> NOW <span class="price-now">$47</span></p>
    <p><span class="hi">10X10</span> STANDARD- WAS <s>$165</s> NOW <span class="price-now">$149</span></p>
    <p>CUSTOMIZED <span class="hi">LEASE &amp; PAYMENT</span> OPTIONS -<br>PACKING, MOVING &amp; STORAGE SUPPLIES</p>
    <p><span class="hi">24 HOUR</span> CODED GATE ACCESS -<br>MOTION SENSOR PROPERTY LIGHTS</p>
    <p>SOPHISTICATED <span class="hi">SURVEILLANCE</span> -<br>DAILY PROPERTY INSPECTIONS</p>
  </div>

  <p class="promo-bar">WE SELL LOCKS, BOXES &amp; PACKING SUPPLIES!</p>
</section>

</body>
</html>
```